Verpackungsdesign für Lifestyle-Diagnostik und Supplements im Bereich Longevity
Zielgruppe
Wir machen Lifestyle-Diagnostik und Supplements im Bereich Longevity
Aufgabenstellung
Verpackung eines Tests (wie der hier: https://shop.quellmora.com/products/zentrip) in der gezeigten Metallschachtel, Supplements in den gezeigten Dosen. Ein Set besteht aus einem Test und zwei Dosen (morgens und abends). Farbschema und Logo Korunelle wie im Anhang. paar Details zu den Supplements auch in den Dateien
Bitte auch an Prägung und anderen Gestaltungsmöglichkeiten denken

```html
<!DOCTYPE html>
<html lang="de">
<head>
<meta charset="utf-8">
<title>Korunelle – Tages- &amp; Nacht-Formel Verpackung</title>
<link href="https://fonts.googleapis.com/css2?family=Montserrat:wght@400;500;600;700&display=swap" rel="stylesheet">
<style>
  :root {
    --teal-top: #23646b;
    --teal-bottom: #1f4d56;
    --lime-top: #a8c723;
    --lime-bottom: #8faa26;
    --lime-text: #a7c52a;
    --dark-text: #1f4e57;
    --white: #ffffff;
    --silver-light: #c9cbcd;
    --silver-dark: #9ea1a4;
    --emboss: #8c8f92;
    --emboss-accent: #7c8a2c;
  }
  * { box-sizing: border-box; margin: 0; padding: 0; }
  html, body { width: 709px; height: 1200px; overflow: hidden; }
  body {
    position: relative;
    background: #ffffff;
    font-family: "Montserrat", sans-serif;
  }

  /* Flat labels */
  .label {
    position: absolute;
    left: 181px;
    width: 359px;
    height: 180px;
    color: var(--white);
    text-align: center;
  }
  .label--night { top: 21px; background: linear-gradient(180deg, var(--teal-top), var(--teal-bottom)); }
  .label--day { top: 232px; background: linear-gradient(180deg, var(--lime-top), var(--lime-bottom)); }

  .brand {
    position: absolute;
    left: 0; right: 0;
    display: flex;
    justify-content: center;
    align-items: center;
    gap: 5px;
    font-weight: 700;
    line-height: 1.2;
    color: var(--white);
  }
  .brand__dot {
    width: 7px; height: 7px;
    border-radius: 50%;
    background: var(--lime-text);
  }
  .label--day .brand__dot,
  .can--day .brand__dot { background: var(--dark-text); }

  .label .brand { top: 43px; font-size: 15px; }
  .product-name {
    position: absolute;
    left: 0; right: 0;
    font-weight: 700;
    line-height: 1.2;
  }
  .label .product-name { top: 80px; font-size: 15px; }
  .label--night .product-name,
  .can--night .product-name { color: var(--lime-text); }
  .label--day .product-name,
  .can--day .product-name { color: var(--dark-text); }

  .icon { position: absolute; left: 50%; transform: translateX(-50%); }
  .label .icon { top: 109px; width: 32px; height: 32px; }

  .tagline {
    position: absolute;
    left: 0; right: 0;
    font-weight: 500;
    line-height: 1.2;
    color: var(--white);
  }
  .label .tagline { top: 151px; font-size: 9.5px; }

  .ingredients {
    position: absolute;
    left: 318px;
    top: 161px;
    transform: rotate(-90deg);
    transform-origin: 0 0;
    white-space: nowrap;
    text-align: left;
    font-size: 7px;
    line-height: 10px;
  }
  .ingredients__intro { font-weight: 400; color: var(--white); }
  .ingredients__list { font-weight: 700; }
  .label--night .ingredients__list { color: var(--lime-text); }
  .label--day .ingredients__list { color: var(--dark-text); }

  /* Embossed tin lid */
  .lid {
    position: absolute;
    top: 470px;
    width: 320px;
    height: 240px;
    border-radius: 4px;
    background: linear-gradient(150deg, var(--silver-light), var(--silver-dark));
    text-align: center;
  }
  .lid--day { left: 16px; }
  .lid--night { left: 373px; }
  .lid .brand {
    top: 88px;
    font-size: 34px;
    color: var(--emboss);
  }
  .lid .brand__dot { width: 10px; height: 10px; background: var(--emboss); }
  .lid__tagline {
    position: absolute;
    left: 0; right: 0;
    top: 138px;
    font-size: 11px;
    font-weight: 600;
    color: var(--emboss-accent);
  }

  /* Flat can wraps */
  .can {
    position: absolute;
    top: 868px;
    width: 160px;
    height: 292px;
    text-align: center;
  }
  .can--day { left: 122px; background: linear-gradient(180deg, var(--lime-top), var(--lime-bottom)); }
  .can--night { left: 419px; background: linear-gradient(180deg, var(--teal-top), var(--teal-bottom)); }
  .can .brand { top: 80px; font-size: 20px; }
  .can .product-name { top: 133px; font-size: 19px; }
  .can .icon { top: 186px; width: 42px; height: 42px; }
  .can .tagline { top: 251px; font-size: 10.5px; }
</style>
</head>
<body>

  <section class="label label--night" aria-label="Etikett Nacht-Formel">
    <div class="brand"><span class="brand__dot"></span>Korunelle</div>
    <div class="product-name">Nacht-Formel</div>
    <svg class="icon icon--moon" viewBox="0 0 40 40" aria-hidden="true">
      <path d="M17 5 A16 16 0 1 0 35 26 A13 13 0 0 1 17 5 Z" fill="none" stroke="#a7c52a" stroke-width="4" stroke-linejoin="round"/>
    </svg>
    <div class="tagline">Täglich ein Schritt voraus</div>
    <div class="ingredients">
      <div class="ingredients__intro">Hochreine Longevity-Wirkstoffe:</div>
      <div class="ingredients__list">NMN, Fisetin</div>
    </div>
  </section>

  <section class="label label--day" aria-label="Etikett Tages-Formel">
    <div class="brand"><span class="brand__dot"></span>Korunelle</div>
    <div class="product-name">Tages-Formel</div>
    <svg class="icon icon--sun" viewBox="0 0 40 40" aria-hidden="true">
      <g fill="none" stroke="#1f4e57" stroke-width="3.5" stroke-linecap="round">
        <circle cx="20" cy="20" r="7.5"/>
        <line x1="20" y1="2" x2="20" y2="6"/><line x1="20" y1="34" x2="20" y2="38"/>
        <line x1="2" y1="20" x2="6" y2="20"/><line x1="34" y1="20" x2="38" y2="20"/>
        <line x1="7.3" y1="7.3" x2="9.8" y2="9.8"/><line x1="30.2" y1="30.2" x2="32.7" y2="32.7"/>
        <line x1="7.3" y1="32.7" x2="9.8" y2="30.2"/><line x1="30.2" y1="9.8" x2="32.7" y2="7.3"/>
      </g>
    </svg>
    <div class="tagline">Täglich ein Schritt voraus</div>
    <div class="ingredients">
      <div class="ingredients__intro">Hochreine Longevity-Wirkstoffe:</div>
      <div class="ingredients__list">NMN, Fisetin</div>
    </div>
  </section>

  <section class="lid lid--day" aria-label="Deckel Metallschachtel mit Prägung">
    <div class="brand"><span class="brand__dot"></span>Korunelle</div>
    <div class="lid__tagline">Täglich ein Schritt voraus</div>
  </section>

  <section class="lid lid--night" aria-label="Deckel Metallschachtel mit Prägung">
    <div class="brand"><span class="brand__dot"></span>Korunelle</div>
    <div class="lid__tagline">Täglich ein Schritt voraus</div>
  </section>

  <section class="can can--day" aria-label="Dosenetikett Tages-Formel">
    <div class="brand"><span class="brand__dot"></span>Korunelle</div>
    <div class="product-name">Tages-Formel</div>
    <svg class="icon icon--sun" viewBox="0 0 40 40" aria-hidden="true">
      <g fill="none" stroke="#1f4e57" stroke-width="3.5" stroke-linecap="round">
        <circle cx="20" cy="20" r="7.5"/>
        <line x1="20" y1="2" x2="20" y2="6"/><line x1="20" y1="34" x2="20" y2="38"/>
        <line x1="2" y1="20" x2="6" y2="20"/><line x1="34" y1="20" x2="38" y2="20"/>
        <line x1="7.3" y1="7.3" x2="9.8" y2="9.8"/><line x1="30.2" y1="30.2" x2="32.7" y2="32.7"/>
        <line x1="7.3" y1="32.7" x2="9.8" y2="30.2"/><line x1="30.2" y1="9.8" x2="32.7" y2="7.3"/>
      </g>
    </svg>
    <div class="tagline">Täglich ein Schritt voraus</div>
  </section>

  <section class="can can--night" aria-label="Dosenetikett Nacht-Formel">
    <div class="brand"><span class="brand__dot"></span>Korunelle</div>
    <div class="product-name">Nacht-Formel</div>
    <svg class="icon icon--moon" viewBox="0 0 40 40" aria-hidden="true">
      <path d="M17 5 A16 16 0 1 0 35 26 A13 13 0 0 1 17 5 Z" fill="none" stroke="#a7c52a" stroke-width="4" stroke-linejoin="round"/>
    </svg>
    <div class="tagline">Täglich ein Schritt voraus</div>
  </section>

</body>
</html>
```